Karateverein Info Plakat
Zielgruppe
Wir sind ein recht junger Karateverein, der Budoverein Sonnenau Riedheim e.V. Zielgruppe sollen hauptsächlich Familien sein, die für Ihr Kind eine Sportart suchen.
Aufgabenstellung
Es soll sich um ein Info Plakat handeln, das wir relativ groß drucken möchten (70cm x 100 cm ) in Hochformat. Grundfarbe sollte in rot gehalten sein. Folgende Infos sollten enthalten sein:
Unser Training fördert:
• körperliche Fitness und Koordination
• Selbstdisziplin und Selbstwertgefühl
• Selbstbewusstsein und Selbstbehauptung
• Selbstverteidigung
• Spaß und Gemeinschaft
In unserem Verein erwartet Dich:
• Kindertraining (ab drei Jahren), Jugendtraining und Erwachsenentraining
• für Anfänger, Fortgeschrittene und Quereinsteiger
• für Breitensportler:innen jeden Alterss und Leistungsgruppen
• Qualifiziertes Trainerteam mit langjähriger Erfahrung und Erfolgsnachweisen
• ein Sport für die ganze Familie
• ein aktives, gemeinschaftliches Vereinsleben
• Training findet auch in den Schulferien statt
• Monatlich kündbare flexible Mitgliedschaft
• Verein ist Mitglied im Nordischen Budobund
• Probetraining ohne Anmeldung möglich

```html
<!DOCTYPE html>
<html lang="de">
<head>
<meta charset="utf-8">
<title>Karateverein Info Plakat</title>
<link rel="stylesheet" href="https://fonts.googleapis.com/css2?family=Source+Sans+3:wght@400;600;700&display=swap">
<style>
  :root {
    --backdrop: #d9d9d6;
    --poster-red: #c8201b;
    --poster-red-deep: #b11913;
    --text-light: #f6e6e4;
    --photo-light: #e9e7e5;
    --photo-mid: #c9c4c0;
    --badge-white: #f7f5f2;
    --badge-ink: #1c1c1c;
    --mascot-teal: #5a9ea6;
    --mascot-deep: #2f6a73;
  }
  * { margin: 0; padding: 0; box-sizing: border-box; }
  html, body { width: 1200px; height: 900px; overflow: hidden; }
  body {
    background: var(--backdrop);
    font-family: "Source Sans 3", sans-serif;
    position: relative;
  }
  .poster {
    position: absolute;
    left: 298px;
    top: 20px;
    width: 604px;
    height: 860px;
    background: linear-gradient(160deg, var(--poster-red) 0%, var(--poster-red-deep) 100%);
    overflow: hidden;
    color: var(--text-light);
  }
  .hero-photo {
    position: absolute;
    left: 62px;
    top: 0;
    width: 542px;
    height: 365px;
    background: linear-gradient(135deg, var(--photo-light) 0%, var(--photo-mid) 100%);
    clip-path: polygon(0 0, 100% 0, 100% 92%, 80% 100%, 58% 90%, 42% 78%, 22% 72%, 9% 56%, 0 40%);
  }
  .club-badge {
    position: absolute;
    left: 30px;
    top: 26px;
    width: 203px;
    height: 203px;
    border-radius: 50%;
    background: var(--badge-white);
    display: flex;
    align-items: center;
    justify-content: center;
    text-align: center;
    padding: 24px;
  }
  .club-name {
    font-weight: 700;
    font-size: 19px;
    line-height: 1.2;
    color: var(--badge-ink);
  }
  .headline {
    position: absolute;
    left: 47px;
    top: 262px;
    font-weight: 600;
    font-size: 39px;
    line-height: 43px;
  }
  .info-block {
    position: absolute;
    left: 47px;
    width: 520px;
  }
  .info-block.benefits { top: 371px; }
  .info-block.offer { top: 525px; }
  .info-title {
    font-weight: 700;
    font-size: 19px;
    line-height: 24px;
  }
  .info-list {
    list-style: none;
    font-size: 16.5px;
    line-height: 21.5px;
  }
  .info-list li {
    padding-left: 9px;
    position: relative;
  }
  .info-list li::before {
    content: "•";
    position: absolute;
    left: 0;
  }
  .mascot {
    position: absolute;
    left: 400px;
    top: 629px;
    width: 202px;
    height: 207px;
    border-radius: 45% 45% 30% 30%;
    background: radial-gradient(circle at 55% 40%, var(--mascot-teal) 0%, var(--mascot-deep) 100%);
  }
</style>
</head>
<body>
  <main class="poster">
    <div class="hero-photo" role="img" aria-label="Foto: Kinder in Karateanzügen mit farbigen Gürteln knien in einer Reihe"></div>

    <div class="club-badge">
      <span class="club-name">Budoverein Sonnenau Riedheim e.V.</span>
    </div>

    <h1 class="headline">Sport für die<br>ganze Familie</h1>

    <section class="info-block benefits">
      <h2 class="info-title">Unser Training fördert:</h2>
      <ul class="info-list">
        <li>körperliche Fitness und Koordination</li>
        <li>Selbstdisziplin und Selbstwertgefühl</li>
        <li>Selbstbewusstsein und Selbstbehauptung</li>
        <li>Selbstverteidigung</li>
        <li>Spaß und Gemeinschaft</li>
      </ul>
    </section>

    <section class="info-block offer">
      <h2 class="info-title">In unserem Verein erwartet Dich:</h2>
      <ul class="info-list">
        <li>Kindertraining (ab drei Jahren), Jugend- und Erwachsenentraining</li>
        <li>für Anfänger, Fortgeschrittene und Quereinsteiger</li>
        <li>für Breitensportler:innen jeden Alterss und Leistungsgruppen</li>
        <li>Qualifiziertes Trainerteam mit langjähriger Erfahrung<br>und Erfolgsnachweisen</li>
        <li>ein Sport für die ganze Familie</li>
        <li>ein aktives, gemeinschaftliches Vereinsleben</li>
        <li>Training findet auch in den Schulferien statt</li>
        <li>Monatlich kündbare flexible Mitgliedschaft</li>
        <li>Verein ist Mitglied im Nordischen Budobund</li>
        <li>Probetraining ohne Anmeldung möglich</li>
      </ul>
    </section>

    <div class="mascot" role="img" aria-label="Illustration: kleiner türkiser Drache im Karateanzug als Vereinsmaskottchen"></div>
  </main>
</body>
</html>
```